A-Stand Directional Sign Design

Objective:
We need a professional graphic design for an A-Stand sign that will guide customers arriving in our parking lot to our office. The design should be visually clear, welcoming, and aligned with our brand identity.
REQUIREMENTS:
Two versions of the design:
- One with an arrow pointing left
- One with an arrow pointing right
(This allows us to place the A-Stand anywhere and flip the graphic as needed.)
DIMENSIONS:
- Viewable Area: 30" x 40"
BRAND ALIGNMENT:
- Colors, fonts, and overall style should match our website: www.skornabel.com
- Clean, modern, and professional look consistent with our aviation/tourism brand
CONTENT:
- Clear directional arrow (left or right depending on version)
- Text: “Office Entrance” or similar concise wording (designers may propose alternatives if they improve clarity)
READABILITY:
- Bold, high-contrast design for visibility from a distance
- Simple layout that avoids clutter
DELIVERABLES:
- Final artwork in print-ready format (PDF preferred)
- Two versions: Arrow Left and Arrow Right
DESIGN GOAL:
Ensure customers can easily find our office upon arrival, while reinforcing skorNABEL’s professional and welcoming brand image.
Target Market(s)
Tourism

```html
<!DOCTYPE html>
<html lang="en">
<head>
<meta charset="utf-8">
<title>skorNABEL – Office Entrance A-Stand Signs</title>
<link href="https://fonts.googleapis.com/css2?family=Anton&display=swap" rel="stylesheet">
<style>
  :root {
    --page-bg: #f4f5f6;
    --brand-blue: #1f6aa8;
    --brand-blue-deep: #175b94;
    --sky-blue: #86b1e4;
    --arrow-blue: #80a8d8;
    --white: #ffffff;
  }
  * { box-sizing: border-box; margin: 0; padding: 0; }
  html, body {
    width: 1200px;
    height: 942px;
    overflow: hidden;
    background: var(--page-bg);
  }
  .canvas {
    position: relative;
    width: 1200px;
    height: 942px;
  }
  .sign {
    position: absolute;
    top: 171px;
    width: 450px;
    height: 600px;
    background: var(--white);
    overflow: hidden;
    box-shadow: 0 2px 10px rgba(0,0,0,0.12);
  }
  .sign--left { left: 120px; }
  .sign--right { left: 630px; }

  .sign__backdrop {
    position: absolute;
    top: 0; left: 0;
    width: 100%;
    height: 472px;
    background: linear-gradient(170deg, var(--brand-blue) 0%, var(--brand-blue-deep) 55%, var(--brand-blue) 100%);
  }
  .brand {
    position: absolute;
    top: 86px;
    left: 0;
    width: 100%;
    display: flex;
    justify-content: center;
    align-items: center;
    gap: 12px;
  }
  .brand__dot {
    width: 26px;
    height: 26px;
    border-radius: 50%;
    background: var(--white);
  }
  .brand__name {
    font-family: "Anton", sans-serif;
    font-size: 40px;
    line-height: 1;
    color: var(--white);
    letter-spacing: 1px;
  }
  .headline {
    position: absolute;
    top: 180px;
    left: 0;
    width: 100%;
    text-align: center;
    font-family: "Anton", sans-serif;
    line-height: 1.05;
    text-transform: uppercase;
  }
  .headline__top {
    display: block;
    font-size: 92px;
    color: var(--sky-blue);
  }
  .headline__bottom {
    display: block;
    font-size: 92px;
    color: var(--white);
  }
  .arrow {
    position: absolute;
    top: 410px;
    left: 0;
    width: 450px;
    height: 130px;
  }
  .arrow--right { transform: scaleX(-1); }
</style>
</head>
<body>
<main class="canvas">

  <section class="sign sign--left" aria-label="Office entrance sign, arrow pointing left">
    <div class="sign__backdrop" role="img" aria-label="Faded helicopter on a helipad, toned in brand blue"></div>
    <div class="brand"><span class="brand__dot"></span><span class="brand__name">skorNABEL</span></div>
    <h1 class="headline"><span class="headline__top">Office</span><span class="headline__bottom">Entrance</span></h1>
    <svg class="arrow arrow--left" viewBox="0 0 450 130" aria-hidden="true">
      <path d="M22 70 L100 8 L132 8 L98 45 L432 40 L432 92 L98 97 L132 128 L100 128 Z"
            fill="var(--arrow-blue)" stroke="var(--white)" stroke-width="4" stroke-linejoin="round"/>
      <path d="M104 22 L42 70 L104 118" fill="none" stroke="var(--white)" stroke-width="1.5" stroke-dasharray="6 5"/>
      <path d="M70 62 L420 56" fill="none" stroke="var(--white)" stroke-width="1.5" stroke-dasharray="6 5"/>
    </svg>
  </section>

  <section class="sign sign--right" aria-label="Office entrance sign, arrow pointing right">
    <div class="sign__backdrop" role="img" aria-label="Faded helicopter on a helipad, toned in brand blue"></div>
    <div class="brand"><span class="brand__dot"></span><span class="brand__name">skorNABEL</span></div>
    <h1 class="headline"><span class="headline__top">Office</span><span class="headline__bottom">Entrance</span></h1>
    <svg class="arrow arrow--right" viewBox="0 0 450 130" aria-hidden="true">
      <path d="M22 70 L100 8 L132 8 L98 45 L432 40 L432 92 L98 97 L132 128 L100 128 Z"
            fill="var(--arrow-blue)" stroke="var(--white)" stroke-width="4" stroke-linejoin="round"/>
      <path d="M104 22 L42 70 L104 118" fill="none" stroke="var(--white)" stroke-width="1.5" stroke-dasharray="6 5"/>
      <path d="M70 62 L420 56" fill="none" stroke="var(--white)" stroke-width="1.5" stroke-dasharray="6 5"/>
    </svg>
  </section>

</main>
</body>
</html>
```